Larkfield Clinic Marketing Flyer

We are a new medical practice in the community and need a flyer to send to other medical offices to inform of our services. We just completed our logo with PixelGuild and would like to incorporate that plus our marketing content into the flyer. Our medical practice has 2 divisions: (1)Mental Health/Psychiatry and (2) Migraine and Neurospasticity Management. Please see website for content and provider photos at www.LarkfieldCare.example

Target Market(s)

Other Healthcare Professionals in the Community

Industry/Entity Type

Medical

Requirements
Must have
• Photos of all 5 healthcare providers, phone number, address, logo

```html
<!DOCTYPE html>
<html lang="en">
<head>
<meta charset="utf-8">
<title>Larkfield Clinic – Services Flyer</title>
<link rel="stylesheet" href="https://fonts.googleapis.com/css2?family=Cinzel:wght@500;700&family=Poppins:wght@400;500;600&display=swap">
<style>
  :root {
    --teal: #11958a;
    --teal-dark: #0f8a7f;
    --lime: #a3d94c;
    --ink: #1d1d1d;
    --band: #e4e4e4;
    --white: #ffffff;
    --backdrop: #f1f3f3;
  }
  * { box-sizing: border-box; margin: 0; padding: 0; }
  html, body { width: 880px; height: 1200px; overflow: hidden; background: var(--backdrop); }
  body { position: relative; font-family: "Poppins", sans-serif; color: var(--ink); }

  .flyer {
    position: absolute; left: 29px; top: 18px;
    width: 1370px; height: 1940px;
    background: var(--white);
    transform: scale(0.6); transform-origin: 0 0;
    overflow: hidden;
  }
  .abs { position: absolute; }

  .top-rule { left: 0; top: 0; width: 100%; height: 24px; background: var(--teal); }

  .brand { left: 48px; top: 66px; width: 364px; text-align: center; color: var(--teal); font-family: "Cinzel", serif; font-weight: 700; }
  .brand-dot { width: 110px; height: 110px; border-radius: 50%; background: var(--teal); margin: 0 auto 14px; }
  .brand-name { font-size: 50px; line-height: 1.05; letter-spacing: 1px; }

  .hero-photo {
    left: 403px; top: 24px; width: 967px; height: 810px;
    background: linear-gradient(100deg, #f4f5f4 0%, #e6e8e6 38%, #b8a58a 55%, #d9a82a 75%, #c99a22 100%);
  }

  .hero-panel { left: 0; top: 323px; width: 755px; height: 457px; background: var(--teal); }
  .headline { left: 49px; top: 385px; font-family: "Cinzel", serif; font-weight: 500; color: var(--white); font-size: 70px; line-height: 78px; letter-spacing: 1px; }
  .headline .accent { color: var(--lime); font-weight: 700; display: block; font-size: 72px; }
  .hero-sub { left: 50px; top: 650px; color: var(--white); font-size: 25px; line-height: 36px; }

  .services-banner {
    left: 232px; top: 925px; width: 906px; height: 98px;
    background: var(--teal); border-radius: 14px;
    color: var(--lime); font-family: "Cinzel", serif; font-weight: 500;
    font-size: 61px; text-align: center; line-height: 100px; letter-spacing: 1px;
  }

  .service { left: 0; width: 100%; text-align: center; }
  .service h2 { color: var(--teal-dark); font-weight: 600; font-size: 30px; line-height: 40px; margin-bottom: 10px; }
  .service p { font-size: 23.5px; line-height: 28px; width: 1100px; margin: 0 auto; }
  .service-mental { top: 1075px; }
  .service-migraine { top: 1259px; }

  .team-band { left: 0; top: 1575px; width: 100%; height: 129px; background: var(--band); }
  .provider { top: 1472px; width: 240px; margin-left: -120px; text-align: center; }
  .provider-frame {
    width: 182px; height: 182px; border-radius: 50%; background: var(--white);
    margin: 0 auto; padding: 5px;
  }
  .provider-ring { width: 100%; height: 100%; border-radius: 50%; border: 3px solid var(--teal); padding: 6px; background: var(--white); }
  .provider-photo { width: 100%; height: 100%; border-radius: 50%; background: radial-gradient(circle at 50% 40%, #8a7e76 0%, #4a5458 70%, #2f3a3e 100%); }
  .provider-name { color: var(--teal-dark); font-size: 24px; margin-top: 12px; }

  .footer { left: 0; top: 1747px; width: 100%; height: 193px; background: var(--teal); color: var(--white); }
  .contact { position: absolute; }
  .contact-label { font-size: 24px; font-weight: 500; line-height: 30px; }
  .contact-line { display: flex; align-items: center; gap: 8px; font-size: 21px; line-height: 28px; }
  .contact-line svg { width: 24px; height: 24px; flex: none; }
  .contact-mental { left: 49px; top: 18px; }
  .contact-migraine { left: 325px; top: 18px; }
  .contact-address { left: 49px; top: 94px; }
  .web { position: absolute; right: 50px; top: 134px; font-size: 18px; letter-spacing: 3px; }
</style>
</head>
<body>
<main class="flyer">
  <div class="abs top-rule"></div>

  <div class="abs brand">
    <div class="brand-dot"></div>
    <div class="brand-name">LARKFIELD<br>CLINIC</div>
  </div>

  <div class="abs hero-photo" role="img" aria-label="Photo of a smiling woman in a yellow top sitting on a sofa, looking at her phone"></div>

  <section class="abs hero-panel"></section>
  <h1 class="abs headline">HELPING BODIES<br>HELPING MINDS<span class="accent">HELPING YOU</span></h1>
  <p class="abs hero-sub">Mental Health and Psychiatry Services<br>Migraine and Neurospasticity Intervention</p>

  <div class="abs services-banner">OUR MEDICAL SERVICES</div>

  <section class="abs service service-mental">
    <h2>MENTAL HEALTH/PSYCHIATRY</h2>
    <p>Bringing comprehensive evaluation, medication management and psychotherapy to the full spectrum of mental health disorders including minor, moderate and major depression, bipolar disorder, ADD/ADHD, anxiety, schizophrenia, stress or grief reactions, and others.</p>
  </section>

  <section class="abs service service-migraine">
    <h2>MIGRAINE AND NEUROSPASTICITY MANAGEMENT</h2>
    <p>Injections of botulinum neurotoxin are a widely used therapeutic form of treatment for both chronic migraines and patients with involuntary muscle contractions (neurospasticity).<br>Injections may offer up to 3 months of relief and may be combined with other<br>pharmaceutical interventions for maximum benefit.</p>
  </section>

  <div class="abs team-band"></div>
  <div class="abs provider" style="left:162px"><div class="provider-frame"><div class="provider-ring"><div class="provider-photo" role="img" aria-label="Portrait of provider Owen Castell"></div></div></div><div class="provider-name">Owen Castell</div></div>
  <div class="abs provider" style="left:415px"><div class="provider-frame"><div class="provider-ring"><div class="provider-photo" role="img" aria-label="Portrait of provider Marlow Quinlan"></div></div></div><div class="provider-name">Marlow Quinlan</div></div>
  <div class="abs provider" style="left:678px"><div class="provider-frame"><div class="provider-ring"><div class="provider-photo" role="img" aria-label="Portrait of provider Ian Tallis"></div></div></div><div class="provider-name">Ian Tallis</div></div>
  <div class="abs provider" style="left:942px"><div class="provider-frame"><div class="provider-ring"><div class="provider-photo" role="img" aria-label="Portrait of provider Vera Ashgrove"></div></div></div><div class="provider-name">Vera Ashgrove</div></div>
  <div class="abs provider" style="left:1202px"><div class="provider-frame"><div class="provider-ring"><div class="provider-photo" role="img" aria-label="Portrait of provider Neil Corbett"></div></div></div><div class="provider-name">Neil Corbett</div></div>

  <footer class="abs footer">
    <div class="contact contact-mental">
      <div class="contact-label">Mental Health</div>
      <div class="contact-line">
        <svg viewBox="0 0 24 24"><circle cx="12" cy="12" r="12" fill="#a3d94c"/><path d="M8 6.5l2 2-1.2 1.6a7 7 0 0 0 5.1 5.1l1.6-1.2 2 2-1.4 1.6c-4.4 0-9.6-5.2-9.6-9.6z" fill="#11958a"/></svg>
        (555)014-2270
      </div>
    </div>
    <div class="contact contact-migraine">
      <div class="contact-label">Migraine and Neurospasticity</div>
      <div class="contact-line">
        <svg viewBox="0 0 24 24"><circle cx="12" cy="12" r="12" fill="#a3d94c"/><path d="M8 6.5l2 2-1.2 1.6a7 7 0 0 0 5.1 5.1l1.6-1.2 2 2-1.4 1.6c-4.4 0-9.6-5.2-9.6-9.6z" fill="#11958a"/></svg>
        (555)014-2270
      </div>
    </div>
    <div class="contact contact-address">
      <div class="contact-label">mailing address</div>
      <div class="contact-line" style="margin-top:8px">
        <svg viewBox="0 0 24 24"><circle cx="12" cy="12" r="12" fill="#a3d94c"/><path d="M12 5a4.5 4.5 0 0 0-4.5 4.5c0 3.4 4.5 8.5 4.5 8.5s4.5-5.1 4.5-8.5A4.5 4.5 0 0 0 12 5zm0 6.2a1.7 1.7 0 1 1 0-3.4 1.7 1.7 0 0 1 0 3.4z" fill="#11958a"/></svg>
        412 W. Alder Ave. Brookhaven, ID&nbsp; 83000
      </div>
    </div>
    <div class="web">WWW.LARKFIELDCARE.EXAMPLE</div>
  </footer>
</main>
</body>
</html>
```